Business Card Design Project

Colette Marvaux logo on front of card with 'of Sydney' added in small font.
Back of card needs to include the following information :

"Pure pleasure for the discerning gentleman" (I may omit once I've seen the design)

colettemarvaux.com.au

Contact by SMS or email only :

colette@colettemarvaux.com.au
Mobile : 0483 615 204 or + 61 483 615 204

Target Market(s)

Male professionals aged 20-60.

Industry/Entity Type

Business

Requirements
Must have
• Simple, bold, stylish and elegant.

```html
<!DOCTYPE html>
<html lang="en">
<head>
<meta charset="utf-8">
<title>Colette Marvaux – Business Card Back</title>
<link rel="stylesheet" href="https://fonts.googleapis.com/css2?family=Open+Sans:wght@400;500&family=Playball&display=swap">
<style>
  :root {
    --card-black: #000000;
    --cream: #f6efdc;
    --glow: rgba(255, 240, 200, 0.55);
    --ivory: #f2f0ea;
    --emblem: #d9d6cf;
  }
  html, body {
    margin: 0;
    padding: 0;
    width: 1200px;
    height: 741px;
    overflow: hidden;
    background: var(--card-black);
  }
  .card-back {
    position: relative;
    width: 1200px;
    height: 741px;
    background: var(--card-black);
  }
  .tagline {
    position: absolute;
    left: 0;
    right: 0;
    top: 345px;
    margin: 0;
    text-align: center;
    font-family: "Playball", cursive;
    font-weight: 400;
    font-size: 38px;
    letter-spacing: 1.5px;
    line-height: 48px;
    color: var(--cream);
    text-shadow: 0 0 3px var(--glow), 0 0 6px var(--glow);
  }
  .contact {
    position: absolute;
    left: 0;
    right: 0;
    top: 394px;
    margin: 0;
    text-align: center;
    font-family: "Open Sans", sans-serif;
    color: var(--ivory);
    font-style: normal;
  }
  .contact-line {
    display: block;
    font-size: 23px;
    line-height: 26px;
    letter-spacing: 1.6px;
  }
  .contact-line.mobile {
    font-size: 17px;
    line-height: 27px;
    letter-spacing: 1.4px;
  }
  .emblem {
    position: absolute;
    left: 588px;
    top: 509px;
    width: 24px;
    height: 24px;
    border-radius: 50%;
    background: radial-gradient(circle, var(--emblem) 0%, #8d8a84 70%, #3a3936 100%);
  }
</style>
</head>
<body>
  <main class="card-back">
    <p class="tagline">”Pure pleasure for the discerning gentleman”</p>
    <address class="contact">
      <span class="contact-line website">colettemarvaux.com.au</span>
      <span class="contact-line note">Contact by SMS or email only :</span>
      <span class="contact-line email">colette@colettemarvaux.com.au</span>
      <span class="contact-line mobile">Mobile : 0483 615 204 or + 61 483 615 204</span>
    </address>
    <div class="emblem" role="img" aria-label="Small floral ornament"></div>
  </main>
</body>
</html>
```